Clara Joy Halden- Lantern Waltz- Autumn/Winter Tour Dates

I need high res A3 Tour poster for print and for social media JPG sharing of tour dates.
Also needed Facebook/Twitter Banner Cover Photos of these dates.
Text Needed Below
Clara Joy Halden
Lantern Waltz
Autumn/Winter Tour Dates
03/09 Ravensby Folk Festival
21/09 Swindon- Calder Theatre
01/10 Hitchin- Brackwell Folk Club
17/10 Bath- The Anvil
20/10 Sheffield- Upper Dale Croquet Club
24/10 Birmingham- Orchard Lamp Cafe
26/10 Glasgow- The Nook and Jar
27/10 Edinburgh - The Marble Parlour
08/11 Capital Reel and Ballad Festival- The Crooked Heron
25/11 Lewes- Tandem Record Shop- Live In Store
02/12 Cambridge- The Quayside
27/01 Lincolnshire- Fenmarsh Theatre
Tickets/Info: www.clarajoyhalden-music.example/gigs
(Quotes/Reviews To Put On)
"Outstanding, rich and expressive."            "Vibrant and Experimental"
**** BdM                                                               **** Tunepaths
"Impressive and Invigorating"                        "Enchanting" Acoustic Wire UK
tBarks

Updates
I cannot read the tour dates on most of the submissions so far. They need to be visible to viewers.
Thank You.
Please also be as creative and inventive as possible- not bland.

Target Market(s)
Music Fans- Folk Acoustic Americana
Industry/Entity Type
Media
Font styles to use
Requirements
Must have
- My photo featured prominently
- Look classy and not tacky or OTT
- Look elegant, wintery and eye catching
- The dates must be very clear to read
- Links to Website:

Nice to have
- Something innovative and not boring in terms of layout design
- Perhaps fading/ misty or wintery

Should not have
- Any colours that do not match

```html
<!DOCTYPE html>
<html lang="en">
<head>
<meta charset="utf-8">
<title>Clara Joy Halden – Lantern Waltz Tour Poster</title>
<link rel="stylesheet" href="https://fonts.googleapis.com/css2?family=Marcellus+SC&family=Raleway:wght@500;700&family=Pinyon+Script&display=swap">
<style>
  :root {
    --backdrop: #e4e4e4;
    --paper: #ffffff;
    --title-blue: #1f63b4;
    --night: #12315f;
    --night-deep: #081a3a;
    --date-blue: #79aaea;
    --text-light: #f2f6fc;
    --rule: rgba(220, 232, 250, 0.7);
  }
  html, body {
    margin: 0;
    width: 1200px;
    height: 1200px;
    overflow: hidden;
    background: radial-gradient(circle at 50% 45%, #f3f3f3 0%, var(--backdrop) 70%, #d2d2d2 100%);
  }
  .poster {
    position: absolute;
    left: 218px;
    top: 60px;
    width: 765px;
    height: 1080px;
    overflow: hidden;
    background: linear-gradient(180deg, #1d3f72 25%, var(--night) 55%, var(--night-deep) 100%);
    box-shadow: 0 4px 14px rgba(0,0,0,0.18);
  }
  .poster__portrait {
    position: absolute;
    left: 400px; top: 250px;
    width: 365px; height: 830px;
    background:
      radial-gradient(ellipse 34% 22% at 55% 30%, #c6d3ea 0%, #8ea7d0 45%, rgba(70,100,150,0) 100%),
      radial-gradient(ellipse 70% 55% at 60% 35%, #2a4a7d 0%, #15294d 60%, rgba(12,28,58,0) 100%),
      linear-gradient(180deg, #3e5f92 0%, #1a3462 45%, #0b1c3d 100%);
    -webkit-mask-image: linear-gradient(90deg, transparent 0%, #000 22%);
    mask-image: linear-gradient(90deg, transparent 0%, #000 22%);
  }
  .poster__header {
    position: absolute;
    left: 0; top: 0;
    width: 100%;
    height: 150px;
    background: var(--paper);
    text-align: center;
  }
  .poster__artist, .poster__album {
    margin: 0;
    font-family: "Marcellus SC", serif;
    font-weight: 400;
    color: var(--title-blue);
    font-size: 52px;
    line-height: 1;
    letter-spacing: 1px;
  }
  .poster__artist { padding-top: 28px; }
  .poster__album { margin-top: 8px; }
  .poster__snowfall {
    position: absolute;
    left: 0; top: 140px;
    width: 765px; height: 240px;
  }
  .tour__heading {
    position: absolute;
    left: 66px; top: 345px;
    margin: 0;
    font-family: "Marcellus SC", serif;
    font-weight: 400;
    font-size: 39px;
    line-height: 42px;
    color: var(--text-light);
  }
  .tour__dates {
    position: absolute;
    left: 66px; top: 452px;
    margin: 0; padding: 0;
    list-style: none;
    font-family: "Raleway", sans-serif;
    font-size: 14px;
    font-weight: 500;
    color: var(--text-light);
  }
  .tour__date-item { display: flex; line-height: 32.8px; }
  .tour__day { width: 52px; flex: none; color: var(--date-blue); font-weight: 700; }
  .tour__venue { white-space: nowrap; }
  .tickets {
    position: absolute;
    left: 192px; top: 934px;
    width: 380px; height: 36px;
    margin: 0;
    border-top: 1px solid var(--rule);
    border-bottom: 1px solid var(--rule);
    font-family: "Raleway", sans-serif;
    font-size: 13.5px;
    line-height: 36px;
    text-align: center;
    white-space: nowrap;
    color: var(--text-light);
  }
  .tickets__label { color: var(--date-blue); font-weight: 700; font-size: 15px; }
  .review {
    position: absolute;
    top: 988px;
    margin: 0;
    font-family: "Pinyon Script", cursive;
    font-size: 26px;
    line-height: 36px;
    white-space: nowrap;
    color: var(--text-light);
  }
  .review--first { left: 74px; }
  .review--second { left: 422px; }
  .review__mark { font-family: Georgia, serif; font-weight: 700; font-size: 28px; vertical-align: 6px; }
</style>
</head>
<body>
  <main class="poster">
    <div class="poster__portrait" role="img" aria-label="Portrait photograph of the singer in a jewelled winter crown, gazing upward among falling snow"></div>

    <svg class="poster__snowfall" role="img" aria-label="Border of white snowflakes and falling snow" viewBox="0 0 765 240" preserveAspectRatio="none">
      <defs>
        <linearGradient id="snowFade" x1="0" y1="0" x2="0" y2="1">
          <stop offset="0" stop-color="#ffffff"/>
          <stop offset="0.45" stop-color="#eef3fb" stop-opacity="0.95"/>
          <stop offset="0.75" stop-color="#a9bedf" stop-opacity="0.55"/>
          <stop offset="1" stop-color="#1d3f72" stop-opacity="0"/>
        </linearGradient>
      </defs>
      <path d="M0 0 H765 V150 C720 175 690 130 640 160 C590 190 560 140 500 165 C450 185 420 130 360 150 C300 170 270 120 210 145 C160 165 120 125 70 150 C40 165 20 140 0 155 Z" fill="url(#snowFade)"/>
      <path d="M0 0 H765 V60 C700 85 660 50 600 75 C540 100 500 60 440 80 C380 100 340 55 280 75 C220 95 180 60 120 80 C70 95 40 70 0 85 Z" fill="#ffffff"/>
    </svg>

    <header class="poster__header">
      <h1 class="poster__artist">Clara Joy Halden</h1>
      <h2 class="poster__album">Lantern Waltz</h2>
    </header>

    <h3 class="tour__heading">Autumn/Winter<br>Tour Dates</h3>

    <ul class="tour__dates">
      <li class="tour__date-item"><span class="tour__day">03/09</span><span class="tour__venue">Ravensby Folk Festival</span></li>
      <li class="tour__date-item"><span class="tour__day">21/09</span><span class="tour__venue">Swindon- Calder Theatre</span></li>
      <li class="tour__date-item"><span class="tour__day">01/10</span><span class="tour__venue">Hitchin- Brackwell Folk Club</span></li>
      <li class="tour__date-item"><span class="tour__day">17/10</span><span class="tour__venue">Bath- The Anvil</span></li>
      <li class="tour__date-item"><span class="tour__day">20/10</span><span class="tour__venue">Sheffield- Upper Dale Croquet Club</span></li>
      <li class="tour__date-item"><span class="tour__day">24/10</span><span class="tour__venue">Birmingham- Orchard Lamp Cafe</span></li>
      <li class="tour__date-item"><span class="tour__day">26/10</span><span class="tour__venue">Glasgow- The Nook and Jar</span></li>
      <li class="tour__date-item"><span class="tour__day">27/10</span><span class="tour__venue">Edinburgh - The Marble Parlour</span></li>
      <li class="tour__date-item"><span class="tour__day">08/11</span><span class="tour__venue">Capital Reel and Ballad Festival-<br>The Crooked Heron</span></li>
      <li class="tour__date-item"><span class="tour__day">25/11</span><span class="tour__venue">Lewes- Tandem Record Shop- Live In Store</span></li>
      <li class="tour__date-item"><span class="tour__day">02/12</span><span class="tour__venue">Cambridge- The Quayside</span></li>
      <li class="tour__date-item"><span class="tour__day">27/01</span><span class="tour__venue">Lincolnshire- Fenmarsh Theatre</span></li>
    </ul>

    <p class="tickets"><span class="tickets__label">Tickets/Info:</span> www.clarajoyhalden-music.example/gigs</p>

    <p class="review review--first"><span class="review__mark">“</span> Outstanding, rich and expressive. <span class="review__mark">”</span></p>
    <p class="review review--second"><span class="review__mark">“</span> Vibrant and Experimental <span class="review__mark">”</span></p>
  </main>
</body>
</html>
```